Tidewell building company Business card design

I need a business card design for my company. I have a logo but dont have business cards with our logo..

www.tidewellbuildingco.com.au

The logo is on the website

I need the same details as this design I have attached. we have changed the logo and colours. just like the website

```html
<!DOCTYPE html>
<html lang="en">
<head>
<meta charset="utf-8">
<title>Tidewell Building – Business Card</title>
<link href="https://fonts.googleapis.com/css2?family=Cinzel:wght@600&family=Tinos&family=Arimo&family=Open+Sans&display=swap" rel="stylesheet">
<style>
  :root {
    --backdrop: #4d5a5b;
    --card-white: #ffffff;
    --ink: #111111;
    --band-dark: #121314;
    --accent-orange: #f5a11f;
    --brand-blue: #3aa2e6;
    --back-dark: #1c1a19;
    --back-glow: #2e2924;
  }
  * { margin: 0; padding: 0; box-sizing: border-box; }
  html, body { width: 900px; height: 1200px; overflow: hidden; }
  body { background: var(--backdrop); position: relative; font-family: "Tinos", serif; }

  .card { position: absolute; overflow: hidden; }
  .card-front { left: 35px; top: 63px; width: 820px; height: 469px; background: var(--card-white); }
  .front-band { position: absolute; left: 0; top: 389px; width: 100%; height: 61px; background: var(--band-dark); }
  .front-stripe { position: absolute; left: 0; top: 450px; width: 100%; height: 19px; background: var(--accent-orange); }
  .front-divider { position: absolute; left: 420px; top: 22px; width: 2px; height: 345px; background: var(--ink); }

  .wordmark { position: absolute; text-align: center; font-family: "Cinzel", serif; font-weight: 600; color: var(--brand-blue); line-height: 1; }
  .wordmark .word-main { display: block; font-size: 48px; letter-spacing: 1px; }
  .wordmark .word-sub { display: block; font-size: 27px; letter-spacing: 9px; margin-top: 6px; }
  .card-front .wordmark { left: 40px; width: 330px; top: 215px; }

  .front-rule { position: absolute; left: 60px; top: 305px; width: 293px; height: 1px; background: var(--ink); }
  .tagline { position: absolute; text-align: center; line-height: 1.18; }
  .card-front .tagline { left: 20px; width: 370px; top: 317px; font-size: 19px; color: var(--ink); }

  .person-name { position: absolute; right: 50px; top: 36px; font-family: "Cinzel", serif; font-weight: 600; font-size: 38px; letter-spacing: 1px; color: var(--ink); }
  .person-role { position: absolute; right: 48px; top: 86px; font-family: "Arimo", sans-serif; font-size: 24px; color: var(--accent-orange); }

  .contact-list { position: absolute; left: 462px; top: 180px; list-style: none; }
  .contact-item { display: flex; align-items: center; height: 52px; }
  .contact-item svg { width: 30px; height: 30px; margin-right: 31px; flex: none; }
  .contact-text { font-size: 20px; color: var(--ink); }
  .contact-email { font-family: "Open Sans", sans-serif; font-size: 16px; }

  .card-back { left: 35px; top: 631px; width: 827px; height: 473px;
    background: radial-gradient(ellipse at 50% 40%, var(--back-glow) 0%, var(--back-dark) 65%, #151414 100%); }
  .card-back .wordmark { left: 0; width: 827px; top: 236px; }
  .card-back .wordmark .word-main { font-size: 54px; }
  .card-back .wordmark .word-sub { font-size: 30px; letter-spacing: 11px; }
  .back-rule { position: absolute; top: 350px; width: 132px; height: 1px; background: var(--accent-orange); }
  .back-rule.left { left: 31px; }
  .back-rule.right { left: 665px; }
  .card-back .tagline { left: 0; width: 827px; top: 335px; font-size: 26px; color: var(--accent-orange); }
</style>
</head>
<body>

<section class="card card-front">
  <div class="wordmark"><span class="word-main">TIDEWELL</span><span class="word-sub">BUILDING</span></div>
  <div class="front-rule"></div>
  <p class="tagline">New Home - Additions &amp; Renovations<br>Domestic &amp; commercial builders</p>

  <div class="front-divider"></div>

  <h1 class="person-name">MARA VELDEN</h1>
  <p class="person-role">Director</p>

  <ul class="contact-list">
    <li class="contact-item">
      <svg viewBox="0 0 30 30" aria-hidden="true"><path d="M3 11c0-4 6-6 12-6s12 2 12 6v2h-6v-3c-2-1-10-1-12 0v3H3z" fill="#f5a11f"/><path d="M8 14h14l3 11H5z" fill="#f5a11f"/><circle cx="15" cy="19.5" r="3" fill="#fff"/></svg>
      <span class="contact-text">08 9417 2635</span>
    </li>
    <li class="contact-item">
      <svg viewBox="0 0 30 30" aria-hidden="true"><rect x="8" y="2" width="14" height="26" rx="3" fill="#f5a11f"/><rect x="11" y="6" width="8" height="12" fill="#fff"/><circle cx="15" cy="23" r="1.8" fill="#fff"/></svg>
      <span class="contact-text">08 9417 2635</span>
    </li>
    <li class="contact-item">
      <svg viewBox="0 0 30 30" aria-hidden="true"><rect x="1" y="10" width="6" height="18" rx="2" fill="#f5a11f"/><rect x="8" y="12" width="21" height="16" rx="2" fill="#f5a11f"/><rect x="12" y="2" width="12" height="12" fill="#f5a11f"/><rect x="14" y="5" width="8" height="1.6" fill="#fff"/><rect x="14" y="8" width="8" height="1.6" fill="#fff"/></svg>
      <span class="contact-text">0422 58 3 164</span>
    </li>
    <li class="contact-item">
      <svg viewBox="0 0 30 30" aria-hidden="true"><rect x="3" y="7" width="24" height="17" rx="2" fill="#f5a11f"/><path d="M4 9l11 8 11-8" fill="none" stroke="#fff" stroke-width="2"/></svg>
      <span class="contact-text contact-email">tidewellbuildingco@postmail.com</span>
    </li>
  </ul>

  <div class="front-band"></div>
  <div class="front-stripe"></div>
</section>

<section class="card card-back">
  <div class="wordmark"><span class="word-main">TIDEWELL</span><span class="word-sub">BUILDING</span></div>
  <div class="back-rule left"></div>
  <div class="back-rule right"></div>
  <p class="tagline">New Home - Additions &amp; Renovations<br>Domestic &amp; commercial builders</p>
</section>

</body>
</html>
```